Brook Forge - Crypto Currency Miner Powered by Renewable Energy Website

We Need Web Pages Design for Website for Crypto Currency Miner

Serivices include:
Mining Rig Sales
Housing for Rigs turnkey on renewable energy grid
Cloud Mining term packages
Updates

http://www.vaultrigdigest.example (Competitors sites)

Target Market(s)

Investers for Mining Rigs and terms for 1,2 or 3 years of Hash rate

Industry/Entity Type

Mining

Number of Pages Required

5+ page

Font styles to use
Sans Serif

Colors
add136
9bcb3c
606060
474747
ffc214
cadf82
fbee3e
876aae
6b449b

Requirements
Must have
• Pictures of Solar, Wind and power Factor Correction units
Nice to have
• e-commerce platform so contract terms can be purchased through website
Should not have
• Heavy construction equipment

```html
<!DOCTYPE html>
<html lang="en">
<head>
<meta charset="utf-8">
<title>Brook Forge — Crypto Currency Miner</title>
<link rel="stylesheet" href="https://fonts.googleapis.com/css2?family=Ubuntu:wght@400;500;700&family=Open+Sans:wght@400;600;700&display=swap">
<style>
:root{
  --green:#add136;
  --green-mid:#9bcb3c;
  --grey:#606060;
  --grey-dark:#474747;
  --yellow:#ffc214;
  --lime-soft:#cadf82;
  --yellow-bright:#fbee3e;
  --purple:#876aae;
  --purple-dark:#6b449b;
  --ink:#2b2b2b;
  --footer:#2a2a2a;
  --footer-bar:#1e1e1e;
  --lilac:#f1eef7;
}
*{box-sizing:border-box;margin:0;padding:0}
html,body{width:1200px;height:2648px;overflow:hidden}
body{font-family:"Open Sans",Arial,sans-serif;color:var(--grey);background:#fff;position:relative}
h1,h2,h3,h4{font-family:"Ubuntu",Arial,sans-serif}
.btn{display:inline-block;font-family:"Ubuntu",Arial,sans-serif;font-size:12px;font-weight:500;text-transform:uppercase;letter-spacing:.5px;padding:11px 26px;border-radius:22px;color:#fff;background:var(--purple);text-decoration:none}
.btn--light{background:#fff;color:var(--grey-dark)}

/* hero */
.hero{position:absolute;left:0;top:0;width:1200px;height:655px;overflow:hidden}
.hero__photo{position:absolute;inset:0;background:linear-gradient(120deg,#e8c21a 0%,#c9c82a 30%,#a9c53a 55%,#8fbf3e 80%,#7cb23a 100%)}
.hero__photo::after{content:"";position:absolute;inset:0;background:linear-gradient(180deg,rgba(0,0,0,.05),rgba(0,0,0,.15))}
.nav{position:absolute;top:0;left:0;width:100%;height:92px;display:flex;align-items:center;padding:0 196px}
.brand{display:flex;align-items:center;gap:8px;font-family:"Ubuntu",Arial,sans-serif;font-weight:700;font-size:20px;color:#fff}
.brand__dot{width:14px;height:14px;border-radius:50%;background:#fff}
.nav__menu{margin-left:auto;display:flex;gap:0;list-style:none;font-family:"Ubuntu",Arial,sans-serif;font-size:12px}
.nav__menu li{padding:24px 13px;color:#fff}
.nav__menu li.is-active{background:#fff;color:var(--grey-dark)}
.hero__content{position:absolute;top:232px;left:0;width:100%;text-align:center;color:#fff}
.hero__title{font-size:58px;font-weight:500;line-height:1.08}
.hero__text{width:560px;margin:22px auto 30px;font-size:12px;line-height:1.6}
.hero__actions{display:flex;justify-content:center;gap:18px}
.hero__arrow{position:absolute;top:364px;width:30px;height:30px;background:rgba(255,255,255,.85);display:flex;align-items:center;justify-content:center}
.hero__arrow--prev{left:0}.hero__arrow--next{right:0}

/* about */
.about{position:absolute;top:655px;left:0;width:1200px;height:297px;display:flex;padding:112px 196px 0}
.about__head{width:215px;text-align:right;padding-right:24px;border-right:2px solid var(--grey-dark);height:62px}
.about__head h2{font-size:30px;font-weight:500;color:var(--ink)}
.about__head p{font-size:10px;font-weight:700;color:var(--grey-dark);text-transform:uppercase;margin-top:4px}
.about__body{padding-left:28px;width:590px}
.about__body p{font-size:11.5px;line-height:1.7}
.about__body .btn{margin-top:22px;padding:9px 20px;font-size:10px}

/* services */
.services{position:absolute;top:952px;left:0;width:1200px;height:448px;display:flex}
.services__list{width:600px;height:100%;background:linear-gradient(160deg,#3b3b3b,#252525);padding:66px 0 0 196px;color:#fff}
.svc{display:flex;align-items:flex-start;gap:16px;margin-bottom:38px}
.svc__icon{flex:none;width:56px;height:56px;border-radius:50%;background:#fff;display:flex;align-items:center;justify-content:center}
.svc h3{font-size:13px;font-weight:500;text-transform:uppercase;margin-top:6px}
.svc p{font-size:11px;line-height:1.5;margin-top:5px;width:250px;color:#ddd}
.services__feature{position:relative;width:600px;height:100%;overflow:hidden}
.services__photo{position:absolute;inset:0;background:linear-gradient(180deg,#f4f5f6 0%,#e8eaec 45%,#9aa4ad 62%,#4d5865 85%,#39424d 100%)}
.services__copy{position:relative;text-align:center;padding-top:96px;color:var(--ink)}
.services__copy h2{font-size:30px;font-weight:500;text-transform:uppercase}
.services__copy p{width:300px;margin:8px auto 20px;font-size:10.5px;font-weight:700;text-transform:uppercase;line-height:1.5;color:var(--grey-dark)}

/* contract terms */
.terms{position:absolute;top:1400px;left:0;width:1200px;height:415px;background:var(--lilac);text-align:center;padding-top:62px}
.terms h2{font-size:28px;font-weight:500;color:var(--ink);text-transform:uppercase}
.terms__sub{font-size:10.5px;font-weight:700;text-transform:uppercase;color:var(--grey-dark);margin-top:6px}
.terms__grid{display:flex;justify-content:center;gap:84px;margin-top:48px}
.term{width:190px;height:190px;border-radius:50%;background:#fff;border:2px solid #ddd6ea;display:flex;flex-direction:column;align-items:center;justify-content:center;padding:0 30px}
.term h3{font-size:14px;font-weight:500;color:var(--ink);margin-top:12px}
.term p{font-size:10.5px;line-height:1.45;margin-top:6px}

/* call to action */
.cta{position:absolute;top:1815px;left:0;width:1200px;height:365px;overflow:hidden;color:#fff;text-align:center}
.cta__photo{position:absolute;inset:0;background:linear-gradient(180deg,#4a4236 0%,#3c3a33 55%,#2c2c28 100%)}
.cta__inner{position:relative;padding-top:104px}
.cta h2{font-size:34px;font-weight:500;text-transform:uppercase}
.cta p{width:430px;margin:14px auto 22px;font-size:11px;line-height:1.6}

/* newsletter */
.newsletter{position:absolute;top:2180px;left:0;width:1200px;height:170px;display:flex;align-items:center;padding:0 196px}
.newsletter__head{width:215px;text-align:right;padding-right:24px;border-right:2px solid var(--grey-dark)}
.newsletter__head h2{font-size:22px;font-weight:500;color:var(--ink);text-transform:uppercase}
.newsletter__head p{font-size:10px;font-weight:700;text-transform:uppercase;color:var(--grey-dark);margin-top:3px}
.newsletter__form{display:flex;align-items:center;margin-left:120px;gap:12px}
.newsletter__field{width:400px;height:44px;border:1px solid #ddd;border-radius:22px;padding:0 20px;display:flex;align-items:center;font-size:11px;color:#999}
.newsletter__form .btn{padding:13px 40px}

/* footer */
.footer{position:absolute;top:2350px;left:0;width:1200px;height:250px;background:var(--footer);display:flex;padding:44px 196px 0}
.footer__col{width:202px}
.footer__col h4{font-size:12px;font-weight:500;color:var(--yellow);text-transform:uppercase;margin-bottom:14px}
.footer__col ul{list-style:none}
.footer__col li{font-size:10.5px;color:#ddd;margin-bottom:7px}
.contact{display:flex;gap:10px;align-items:flex-start;font-size:10.5px;color:#ddd;margin-bottom:12px;line-height:1.5}
.social{display:flex;gap:8px;margin-bottom:16px}
.social span{width:24px;height:24px;border-radius:50%;border:1.5px solid #ddd}
.footer__bar{position:absolute;top:2600px;left:0;width:1200px;height:48px;background:var(--footer-bar);color:#ccc;font-size:10.5px;display:flex;align-items:center;justify-content:center}
</style>
</head>
<body>

<header class="hero">
  <div class="hero__photo" role="img" aria-label="Wind turbines in a sunlit green field at golden hour"></div>
  <nav class="nav">
    <div class="brand"><span class="brand__dot"></span>Brook Forge</div>
    <ul class="nav__menu">
      <li class="is-active">Home</li><li>About Us</li><li>Services</li><li>Contract Terms</li><li>FAQ</li><li>Contact Us</li><li>&#9679; Login</li>
    </ul>
  </nav>
  <div class="hero__content">
    <h1 class="hero__title">Welcome To Crypto<br>Currency Miner</h1>
    <p class="hero__text">Lorem Ipsum is simply dummy text of the printing and typesetting industry. Lorem Ipsum has been the industry's standard dummy text ever since the 1500s, when an unknown printer took a galley.</p>
    <div class="hero__actions"><span class="btn btn--light">Learn More</span><span class="btn">Contact Us</span></div>
  </div>
  <span class="hero__arrow hero__arrow--prev"><svg width="10" height="10" viewBox="0 0 10 10"><path d="M7 1 3 5l4 4" fill="none" stroke="#474747" stroke-width="1.6"/></svg></span>
  <span class="hero__arrow hero__arrow--next"><svg width="10" height="10" viewBox="0 0 10 10"><path d="M3 1l4 4-4 4" fill="none" stroke="#474747" stroke-width="1.6"/></svg></span>
</header>

<section class="about">
  <div class="about__head"><h2>ABOUT US</h2><p>Lorem ipsum is simply text</p></div>
  <div class="about__body">
    <p>Lorem Ipsum is simply dummy text of the printing and typesetting industry. Lorem Ipsum has been the industry's standard dummy text ever since the 1500s, when an unknown printer took a galley of type and scrambled it to make a type specimen book. It has survived not only five centuries, but also the leap into electronic typesetting, remaining essentially unchanged.</p>
    <span class="btn">Read More</span>
  </div>
</section>

<section class="services">
  <div class="services__list" role="img" aria-label="Dark photo of a solar panel field behind the service list">
    <div class="svc">
      <span class="svc__icon"><svg width="26" height="26" viewBox="0 0 26 26"><path d="M13 3v20M9 23h8M13 10l-6-4M13 10l6-4M13 10v-4" fill="none" stroke="#876aae" stroke-width="2"/></svg></span>
      <div><h3>Mining Rig Sales</h3><p>Lorem Ipsum is simply dummy text of the printing and typesetting industry.</p></div>
    </div>
    <div class="svc">
      <span class="svc__icon"><svg width="26" height="26" viewBox="0 0 26 26"><path d="M4 12 13 4l9 8v10H4z" fill="none" stroke="#876aae" stroke-width="2"/></svg></span>
      <div><h3>Housing for Rigs Turnkey on Renewable...</h3><p>Lorem Ipsum is simply dummy text of the printing and typesetting industry.</p></div>
    </div>
    <div class="svc">
      <span class="svc__icon"><svg width="26" height="26" viewBox="0 0 26 26"><path d="M7 19a5 5 0 0 1 1-10 6 6 0 0 1 11 2 4 4 0 0 1 0 8z" fill="none" stroke="#876aae" stroke-width="2"/></svg></span>
      <div><h3>Cloud Mining Term Packages</h3><p>Lorem Ipsum is simply dummy text of the printing and typesetting industry.</p></div>
    </div>
  </div>
  <div class="services__feature">
    <div class="services__photo" role="img" aria-label="Rows of solar panels under a pale sky"></div>
    <div class="services__copy">
      <h2>Our Services</h2>
      <p>Lorem ipsum is simply dummy text of the printing and typesetting industry</p>
      <span class="btn">View More Services</span>
    </div>
  </div>
</section>

<section class="terms">
  <h2>Purchase Contract Terms</h2>
  <p class="terms__sub">Lorem ipsum is simply dummy text of the printing industry</p>
  <div class="terms__grid">
    <div class="term">
      <svg width="40" height="40" viewBox="0 0 40 40"><rect x="7" y="9" width="26" height="24" rx="2" fill="none" stroke="#876aae" stroke-width="2"/><path d="M7 16h26M13 5v7M27 5v7" stroke="#876aae" stroke-width="2"/></svg>
      <h3>1 Year of Hash rate</h3><p>Lorem Ipsum is simply dummy text</p>
    </div>
    <div class="term">
      <svg width="40" height="40" viewBox="0 0 40 40"><rect x="7" y="9" width="26" height="24" rx="2" fill="none" stroke="#876aae" stroke-width="2"/><path d="M7 16h26M13 5v7M27 5v7" stroke="#876aae" stroke-width="2"/></svg>
      <h3>2 Year of Hash rate</h3><p>Lorem Ipsum is simply dummy text</p>
    </div>
    <div class="term">
      <svg width="40" height="40" viewBox="0 0 40 40"><rect x="7" y="9" width="26" height="24" rx="2" fill="none" stroke="#876aae" stroke-width="2"/><path d="M7 16h26M13 5v7M27 5v7" stroke="#876aae" stroke-width="2"/></svg>
      <h3>3 Year of Hash rate</h3><p>Lorem Ipsum is simply dummy text</p>
    </div>
  </div>
</section>

<section class="cta">
  <div class="cta__photo" role="img" aria-label="Wind turbines on a hillside at dusk"></div>
  <div class="cta__inner">
    <h2>Try Crypto Currency Miner Today</h2>
    <p>Lorem Ipsum is simply dummy text of the printing and typesetting industry. Lorem Ipsum has been the industry's standard dummy text ever since the 1500s, when an unknown printer took a galley.</p>
    <span class="btn">Contact Us</span>
  </div>
</section>

<section class="newsletter">
  <div class="newsletter__head"><h2>Newsletter</h2><p>Lorem ipsum is simply text</p></div>
  <div class="newsletter__form">
    <div class="newsletter__field">Enter Your E-mail</div>
    <span class="btn">Send</span>
  </div>
</section>

<footer class="footer">
  <div class="footer__col"><h4>Company</h4><ul><li>Home</li><li>Services</li><li>About Us</li><li>Contract Terms</li><li>FAQ</li><li>Contact Us</li></ul></div>
  <div class="footer__col"><h4>Quick Links</h4><ul><li>News</li><li>Account</li><li>Login</li><li>Help</li></ul></div>
  <div class="footer__col" style="width:260px">
    <h4>Keep in Touch</h4>
    <div class="contact"><svg width="12" height="12" viewBox="0 0 12 12"><path d="M2 1h3l1 3-2 1a7 7 0 0 0 3 3l1-2 3 1v3c-6 0-10-4-10-9z" fill="#ddd"/></svg>+1 555 014 2880</div>
    <div class="contact"><svg width="12" height="12" viewBox="0 0 12 12"><path d="M6 11S2 7 2 4.5a4 4 0 0 1 8 0C10 7 6 11 6 11z" fill="#ddd"/></svg>Lorem Ipsum is simply dummy text<br>of the printing</div>
    <div class="contact"><svg width="12" height="12" viewBox="0 0 12 12"><rect x="1" y="2.5" width="10" height="7" fill="none" stroke="#ddd"/><path d="M1 3l5 4 5-4" fill="none" stroke="#ddd"/></svg>hello@brookforge.example</div>
  </div>
  <div class="footer__col">
    <h4>Follow Us</h4>
    <div class="social"><span></span><span></span><span></span><span></span></div>
    <ul><li>Privacy Policy</li><li>Terms and Condition</li></ul>
  </div>
</footer>
<div class="footer__bar">© Copyright 2018 Brook Forge. All Rights Reserved.</div>

</body>
</html>
```